Verpackungsdesign einer Faltschachtel für Haarteile & Perücken
Zielgruppe
Wir Produzieren Haarteile und Perücken
www.lunavell.de
Aufgabenstellung
Einen KartonF Faltschachtel in Schuhkartongröße. 20cm 16 cm 12 cm
Unser logo und der text soll auf der schachtel untergebracht werden.
https://www.faltwerkpost.de/krempelverpackung-drucken.html
matte folie
innen und außen druck
Der Karton sollte möglich dunkle farben haben. kann auch gerne fast schwarz sein.
Krempelschachtel - 380g/m² Norda Board - 20 cm x 16 cm x 12 cm - 2000 Stück - 12 Werktage Produktionszeit - 4-farbig bedruckt - Matte Folie - Ohne Heißfolie - Ohne Fenster - 4/4 farbig (aussen+innen)

```html
<!DOCTYPE html>
<html lang="de">
<head>
<meta charset="utf-8">
<title>Lunavell Faltschachtel – Stanzform und Innendruck</title>
<link rel="stylesheet" href="https://fonts.googleapis.com/css2?family=Roboto+Condensed:wght@300;400;700&display=swap">
<style>
  :root{
    --ink:#0b0b0b;
    --paper:#ffffff;
    --gold:#c8a878;
    --gold-line:#a88d62;
    --fold:#b3262b;
    --cut:#86c774;
    --label:#d9d9d9;
    --body:#3a3a3a;
    --field:#f2ece3;
    --photo-a:#7d7873;
    --photo-b:#c7c1bb;
    --muted:#a9a9a9;
  }
  html,body{margin:0;padding:0;background:var(--paper);width:1200px;height:2377px;overflow:hidden}
  .sheet{display:block;width:1200px;height:2377px;font-family:'Roboto Condensed',sans-serif}
  .label{fill:var(--label);font-size:13px;font-weight:300}
  .label-sm{fill:var(--label);font-size:12.5px;font-weight:300}
  .card-title{fill:#111;font-size:13.5px;font-weight:700}
  .card-text{fill:var(--body);font-size:10.5px;font-weight:300}
  .card-strong{fill:#111;font-size:10px;font-weight:700}
  .contact{fill:var(--muted);font-size:10px;font-weight:300}
  .brand{fill:var(--gold);font-weight:300}
  .brand-ring{fill:none;stroke:var(--gold);stroke-width:2}
  .frame{fill:none;stroke:var(--gold-line);stroke-width:1.3}
  .box{fill:var(--paper)}
  .field{fill:var(--field)}
  .fold{stroke:var(--fold);stroke-width:1;fill:none}
  .cutline{fill:var(--paper);stroke:var(--cut);stroke-width:1}
  .panel{fill:var(--ink)}
  .seam{stroke:#3a3a3a;stroke-width:1}
  .photo{fill:url(#photoTone)}
</style>
</head>
<body>
<svg class="sheet" viewBox="0 0 1300 2576" xmlns="http://www.w3.org/2000/svg">
  <defs>
    <linearGradient id="photoTone" x1="0" y1="0" x2="1" y2="1">
      <stop offset="0" stop-color="#c7c1bb"/>
      <stop offset="1" stop-color="#7d7873"/>
    </linearGradient>
    <clipPath id="detailClip"><rect x="343" y="1250" width="914" height="452"/></clipPath>

    <g id="inner-print">
      <line class="fold" x1="540" y1="1305" x2="1072" y2="1305"/>
      <line class="fold" x1="540" y1="1305" x2="540" y2="1702"/>
      <line class="fold" x1="1072" y1="1305" x2="1072" y2="1702"/>

      <!-- linke Seitenwand -->
      <g class="customer-side">
        <rect class="frame" x="351" y="1316" width="163" height="134" rx="4"/>
        <text class="label-sm" transform="translate(374,1420) rotate(-90)" textLength="58" lengthAdjust="spacingAndGlyphs">HAARSYSTEM</text>
        <text class="label-sm" transform="translate(396,1420) rotate(-90)" textLength="90" lengthAdjust="spacingAndGlyphs">HAARVERDICHTUNG</text>
        <text class="label-sm" transform="translate(419,1420) rotate(-90)" textLength="98" lengthAdjust="spacingAndGlyphs">HAARVERLÄNGERUNG</text>
        <text class="label-sm" transform="translate(442,1420) rotate(-90)" textLength="40" lengthAdjust="spacingAndGlyphs">PERÜCKE</text>
        <text class="label-sm" transform="translate(479,1420) rotate(-90)" textLength="92" lengthAdjust="spacingAndGlyphs">MASSANFERTIGUNG</text>
        <text class="label-sm" transform="translate(501,1420) rotate(-90)" textLength="44" lengthAdjust="spacingAndGlyphs">ABDRUCK</text>
        <rect class="box" x="361" y="1427" width="15" height="15"/>
        <rect class="box" x="383" y="1427" width="15" height="15"/>
        <rect class="box" x="406" y="1427" width="15" height="15"/>
        <rect class="box" x="429" y="1427" width="15" height="15"/>
        <rect class="box" x="464" y="1427" width="15" height="15"/>
        <rect class="box" x="488" y="1427" width="15" height="15"/>

        <rect class="box" x="360" y="1460" width="23" height="112"/>
        <rect class="box" x="391" y="1460" width="23" height="112"/>
        <rect class="box" x="422" y="1460" width="23" height="112"/>
        <text class="label" transform="translate(377,1636) rotate(-90)" textLength="56" lengthAdjust="spacingAndGlyphs">NACHNAME</text>
        <text class="label" transform="translate(408,1636) rotate(-90)" textLength="48" lengthAdjust="spacingAndGlyphs">VORNAME</text>
        <text class="label" transform="translate(439,1636) rotate(-90)" textLength="36" lengthAdjust="spacingAndGlyphs">DATUM</text>
        <text class="label" transform="translate(476,1491) rotate(-90)" textLength="29" lengthAdjust="spacingAndGlyphs">MANN</text>
        <rect class="box" x="463" y="1498" width="14" height="14"/>
        <text class="label" transform="translate(476,1550) rotate(-90)" textLength="25" lengthAdjust="spacingAndGlyphs">FRAU</text>
        <rect class="box" x="463" y="1556" width="14" height="14"/>
        <rect class="box" x="360" y="1643" width="84" height="59"/>
      </g>

      <!-- Übergabekarte -->
      <g class="handover-card">
        <rect class="box" x="557" y="1330" width="238" height="313" rx="3"/>
        <text class="card-title" x="567" y="1353" textLength="152" lengthAdjust="spacingAndGlyphs">ÜBERGABE AN DEN KUNDEN</text>
        <text class="card-text" x="567" y="1376" textLength="115" lengthAdjust="spacingAndGlyphs">Datum der Übergabe a. d. Kunden</text>
        <text class="card-text" x="567" y="1389" textLength="110" lengthAdjust="spacingAndGlyphs">(falls leer gilt das Vertragsdatum)</text>
        <rect class="field" x="688" y="1366" width="97" height="20"/>
        <text class="card-text" x="567" y="1413" textLength="202" lengthAdjust="spacingAndGlyphs">Mit meiner Vertragsunterschrift bestätige ich das Haarsystem</text>
        <text class="card-text" x="567" y="1426" textLength="153" lengthAdjust="spacingAndGlyphs">bzw. die Haarverlängerung erhalten zu haben.</text>
        <text class="card-text" x="567" y="1449" textLength="103" lengthAdjust="spacingAndGlyphs">Mir wurde das Produkt mit der</text>
        <g class="checklist">
          <rect class="field" x="567" y="1454" width="7" height="7"/><text class="card-text" x="578" y="1462" textLength="91" lengthAdjust="spacingAndGlyphs">wunschgemäßen Haarfarbe</text>
          <rect class="field" x="567" y="1468" width="7" height="7"/><text class="card-text" x="578" y="1476" textLength="34" lengthAdjust="spacingAndGlyphs">Haarlänge</text>
          <rect class="field" x="567" y="1481" width="7" height="7"/><text class="card-text" x="578" y="1489" textLength="67" lengthAdjust="spacingAndGlyphs">Haardichte &amp; Menge</text>
          <rect class="field" x="567" y="1495" width="7" height="7"/><text class="card-text" x="578" y="1503" textLength="40" lengthAdjust="spacingAndGlyphs">Haarqualität</text>
          <rect class="field" x="567" y="1508" width="7" height="7"/><text class="card-text" x="578" y="1516" textLength="83" lengthAdjust="spacingAndGlyphs">Struktur/Wellung/ Glätte</text>
          <rect class="field" x="567" y="1522" width="7" height="7"/><text class="card-text" x="578" y="1530" textLength="59" lengthAdjust="spacingAndGlyphs">Frisur übergeben.</text>
          <rect class="field" x="567" y="1535" width="7" height="7"/><text class="card-text" x="578" y="1543" textLength="193" lengthAdjust="spacingAndGlyphs">Mit der Länge des Ponys/Gesamtlänge bin ich einverstanden.</text>
          <rect class="field" x="567" y="1548" width="7" height="7"/><text class="card-text" x="578" y="1556" textLength="197" lengthAdjust="spacingAndGlyphs">Alle wunschgemäßen Anpassungsarbeiten wurden fertiggestellt</text>
          <text class="card-text" x="578" y="1569" textLength="180" lengthAdjust="spacingAndGlyphs">und mir das Produkt nach meinen Wünschen übergeben.</text>
        </g>
        <text class="card-text" x="567" y="1592" textLength="190" lengthAdjust="spacingAndGlyphs">Spätere farbliche oder modische Anpassungen sind nicht</text>
        <text class="card-text" x="567" y="1606" textLength="208" lengthAdjust="spacingAndGlyphs">Vertragsbestandteil. Auch dann nicht, wenn die Veränderungen</text>
        <text class="card-text" x="567" y="1619" textLength="204" lengthAdjust="spacingAndGlyphs">durch eigenständige Änderungen des Produkts ausgelöst</text>
        <text class="card-text" x="567" y="1633" textLength="153" lengthAdjust="spacingAndGlyphs">werden oder bei der Besprechung vereinbart.</text>
      </g>

      <!-- Absender -->
      <g class="sender">
        <circle class="brand-ring" cx="577" cy="1661" r="8"/>
        <text class="brand" x="591" y="1667" font-size="17">lunavell</text>
        <text class="contact" x="566" y="1687" textLength="70" lengthAdjust="spacingAndGlyphs">Am Lindenhang 4</text>
        <text class="contact" x="566" y="1699" textLength="72" lengthAdjust="spacingAndGlyphs">79100 Freiburg</text>
        <line x1="666" y1="1655" x2="666" y2="1702" stroke="#a9a9a9" stroke-width="1"/>
        <text class="contact" x="688" y="1663" textLength="103" lengthAdjust="spacingAndGlyphs">+49 (0) 761/4827150-0</text>
        <text class="contact" x="688" y="1675" textLength="99" lengthAdjust="spacingAndGlyphs">+49 (0) 151/20481736</text>
        <text class="contact" x="688" y="1687" textLength="60" lengthAdjust="spacingAndGlyphs">s@lunavell.de</text>
        <text class="contact" x="688" y="1699" textLength="72" lengthAdjust="spacingAndGlyphs">www.lunavell.de</text>
      </g>

      <!-- Pflegehinweise -->
      <g class="care-card">
        <rect class="box" x="815" y="1330" width="237" height="372" rx="3"/>
        <text class="card-text" x="827" y="1349" textLength="210" lengthAdjust="spacingAndGlyphs">Hiermit bestätige ich die Pflegehinweise zu beachten, regelmäßig und</text>
        <text class="card-text" x="827" y="1362" textLength="198" lengthAdjust="spacingAndGlyphs">bei Verschlechterung der Haare den LV-20 Service und ggf. einen</text>
        <text class="card-text" x="827" y="1375" textLength="198" lengthAdjust="spacingAndGlyphs">Färbeservice in Anspruch zu nehmen. Haarnetze müssen ggf. vom</text>
        <text class="card-text" x="827" y="1388" textLength="79" lengthAdjust="spacingAndGlyphs">Friseur versiegelt werden.</text>
        <text class="card-text" x="827" y="1408" textLength="190" lengthAdjust="spacingAndGlyphs">Im Fall eines erheblichen Mangels muss das Haarteil binnen 4</text>
        <text class="card-text" x="827" y="1421" textLength="200" lengthAdjust="spacingAndGlyphs">Wochen zum Hersteller geschickt werden. Es ist für mich zumutbar</text>
        <text class="card-text" x="827" y="1434" textLength="205" lengthAdjust="spacingAndGlyphs">das Haar ggf. zur Überprüfung eines Mangels für 14 Tage, ersatzlos,</text>
        <text class="card-text" x="827" y="1448" textLength="196" lengthAdjust="spacingAndGlyphs">dem Hersteller zu übergeben. Bei jeder chemischen Veränderung</text>
        <text class="card-text" x="827" y="1461" textLength="196" lengthAdjust="spacingAndGlyphs">des Haars verfällt der Anspruch auf Garantie. Nicht jedoch durch</text>
        <text class="card-text" x="827" y="1474" textLength="204" lengthAdjust="spacingAndGlyphs">einmaliges Tönen beim Friseurpartner mit1,9% (oder weniger) und</text>
        <text class="card-text" x="827" y="1487" textLength="194" lengthAdjust="spacingAndGlyphs">maximal 15 Minuten Färbedauer, um das Farbbild der Haare zu</text>
        <text class="card-text" x="827" y="1501" textLength="50" lengthAdjust="spacingAndGlyphs">stabilisieren.</text>
        <text class="card-text" x="827" y="1521" textLength="208" lengthAdjust="spacingAndGlyphs">Ich bin mir darüber im Klaren, dass die Haare farblich und chemisch</text>
        <text class="card-text" x="827" y="1534" textLength="208" lengthAdjust="spacingAndGlyphs">behandelt wurden und dass blonde oder gewellte Haare, auf Grund</text>
        <text class="card-text" x="827" y="1547" textLength="204" lengthAdjust="spacingAndGlyphs">der chemischen Aufhellung, eine extrem hohe Strukturschwächung</text>
        <text class="card-text" x="827" y="1561" textLength="204" lengthAdjust="spacingAndGlyphs">erfahren haben. Sie benötigen eine milde Pflege und besitzen, wie</text>
        <text class="card-text" x="827" y="1574" textLength="200" lengthAdjust="spacingAndGlyphs">auch dauerbefestigte Haarteile, eine erheblich kürzere Produktle-</text>
        <text class="card-text" x="827" y="1587" textLength="35" lengthAdjust="spacingAndGlyphs">bensdauer.</text>
        <text class="card-strong" x="827" y="1611" textLength="25" lengthAdjust="spacingAndGlyphs">Datum</text>
        <rect class="field" x="827" y="1617" width="203" height="22"/>
        <text class="card-strong" x="827" y="1660" textLength="70" lengthAdjust="spacingAndGlyphs">Unterschrift Kunde</text>
        <rect class="field" x="827" y="1666" width="203" height="22"/>
      </g>

      <!-- rechte Seitenwand -->
      <g class="model-side">
        <rect class="frame" x="1111" y="1352" width="111" height="329" rx="4"/>
        <text class="label" transform="translate(1188,1365) rotate(90)" textLength="40" lengthAdjust="spacingAndGlyphs">MODELL</text>
        <text class="label" transform="translate(1157,1365) rotate(90)" textLength="28" lengthAdjust="spacingAndGlyphs">FARBE</text>
        <rect class="box" x="1183" y="1413" width="22" height="250"/>
        <rect class="box" x="1152" y="1413" width="22" height="92"/>
        <text class="label" transform="translate(1157,1518) rotate(90)" textLength="48" lengthAdjust="spacingAndGlyphs">WELLUNG</text>
        <rect class="box" x="1152" y="1572" width="22" height="92"/>
        <rect class="box" x="1125" y="1367" width="14" height="14"/>
        <text class="label" transform="translate(1128,1388) rotate(90)" textLength="59" lengthAdjust="spacingAndGlyphs">HAARSYSTEM</text>
        <rect class="box" x="1125" y="1470" width="14" height="14"/>
        <text class="label" transform="translate(1128,1491) rotate(90)" textLength="40" lengthAdjust="spacingAndGlyphs">PERÜCKE</text>
        <rect class="box" x="1125" y="1553" width="14" height="14"/>
        <text class="label" transform="translate(1128,1574) rotate(90)" textLength="91" lengthAdjust="spacingAndGlyphs">HAARVERDICHTUNG</text>
      </g>
    </g>

    <g id="brand-mark">
      <circle class="brand-ring" cx="-80" cy="-14" r="26"/>
      <text class="brand" x="-44" y="2" font-size="46">lunavell</text>
    </g>
  </defs>

  <g class="dieline">
    <path class="cutline" d="M290,248 C290,130 360,44 453,44 L770,44 C875,44 938,130 938,248 Z"/>
    <path class="cutline" d="M312,500 L312,355 C312,275 368,238 453,237 L770,237 C852,238 903,275 903,355 L903,500 Z"/>
    <rect class="cutline" x="325" y="492" width="573" height="651" rx="14"/>
    <rect class="cutline" x="29" y="682" width="1164" height="271" rx="4"/>

    <path class="panel top-flap" d="M298,240 C298,140 360,55 453,52 L770,52 C870,55 930,140 930,240 Z"/>
    <rect class="photo" x="453" y="52" width="317" height="190" role="img" aria-label="Schwarzweiß-Porträt einer Frau mit langen, gelockten Haaren"/>

    <path class="panel lid" d="M320,497 L320,355 C320,280 370,248 453,245 L770,245 C850,248 895,280 895,355 L895,497 Z"/>
    <rect class="panel" x="333" y="500" width="557" height="635" rx="10"/>
    <rect class="panel" x="37" y="690" width="1148" height="255"/>
    <rect class="photo" x="453" y="500" width="317" height="190" role="img" aria-label="Schwarzweiß-Porträt eines Mannes mit zurückgekämmter Frisur"/>

    <line class="seam" x1="259" y1="690" x2="259" y2="945"/>
    <line class="seam" x1="963" y1="690" x2="963" y2="945"/>
    <line class="fold" x1="453" y1="245" x2="453" y2="1135"/>
    <line class="fold" x1="770" y1="245" x2="770" y2="1135"/>
    <line class="fold" x1="453" y1="497" x2="770" y2="497"/>
    <line class="fold" x1="453" y1="945" x2="770" y2="945"/>
    <line class="fold" x1="70" y1="700" x2="70" y2="730"/>
    <line class="fold" x1="70" y1="780" x2="70" y2="860"/>
    <line class="fold" x1="1153" y1="700" x2="1153" y2="730"/>
    <line class="fold" x1="1153" y1="780" x2="1153" y2="860"/>

    <use href="#brand-mark" transform="translate(610,365) rotate(180) scale(0.95)"/>
    <use href="#brand-mark" transform="translate(610,1048) rotate(180) scale(0.95)"/>
    <text class="contact" font-size="9" text-anchor="middle" transform="translate(572,1013) rotate(180)">www.lunavell.de</text>

    <use href="#inner-print" transform="translate(453,690) scale(0.596) translate(-540,-1305)"/>
  </g>

  <g class="detail" clip-path="url(#detailClip)">
    <rect class="panel" x="343" y="1250" width="914" height="452"/>
    <rect class="photo" x="540" y="1250" width="532" height="55" role="img" aria-label="Ausschnitt des Männerporträts: Kinn und Schultern"/>
    <use href="#inner-print"/>
  </g>
</svg>
</body>
</html>
```